Design trifold flyer for patients

Hi buddy,I need a trifold brochure for an early event that month. I just need a design template in Adobe Illustrator, so that I can modify it later.Size: A4 divide into 3 pages, 10x21cm each. The total has 6 page with both sides.Content: (Page)1. Cover with logo, address, phone number, etc..2. Instruction: An image and a paragraph3 + 4. A content list, paragraph5. Note with patients6. Price listColor: blue and light blue, greenTarget audience: Patients

Target Market(s)

Patients in hospital

Industry/Entity Type

Medical

Font styles to use
Sans Serif

Colors
85cae6
33b8a4
0692cd

Requirements
Must have
• picture place holder
Nice to have
• icon

```html
<!DOCTYPE html>
<html lang="en">
<head>
<meta charset="utf-8">
<title>Riverside Care Hospital – Patient Trifold</title>
<link href="https://fonts.googleapis.com/css2?family=Open+Sans:ital,wght@0,400;0,600;0,700;1,400;1,600&family=Quicksand:wght@400;500;700&family=Ubuntu:wght@500;700&display=swap" rel="stylesheet">
<style>
  :root{
    --royal:#1b3fd0;
    --sky:#3aa6ee;
    --light:#85cae6;
    --pale:#dff1fb;
    --paper:#f7f8f9;
    --ink:#5a5f66;
    --bg:#d8e0e2;
  }
  *{box-sizing:border-box;margin:0;padding:0}
  html,body{width:1200px;height:1200px;overflow:hidden;background:var(--bg)}
  body{font-family:"Open Sans",sans-serif;color:var(--ink);position:relative}
  .spread{position:absolute;left:220px;width:760px;height:537px;display:grid;grid-template-columns:repeat(3,1fr);background:var(--paper);box-shadow:0 10px 24px rgba(0,0,0,.18)}
  .spread--inside{top:48px}
  .spread--outside{top:620px}
  .panel{position:relative;overflow:hidden;padding:22px 18px;border-right:1px solid #e4e8ea}
  .panel:last-child{border-right:none}
  .photo{background:linear-gradient(160deg,#eef4f8,#c9dce8 55%,#a9c3d4)}
  .heading{font-family:"Quicksand",sans-serif;font-weight:500;color:var(--sky);font-size:26px;line-height:1}
  .rule{height:1px;background:var(--light);margin:6px 0 10px}
  .body{font-size:7px;line-height:1.45;font-style:italic}
  .item{margin-bottom:11px}
  .item h3{font-family:"Open Sans",sans-serif;font-size:11px;font-weight:700;font-style:italic;color:var(--royal);display:flex;align-items:center;gap:5px;margin-bottom:3px}
  .item h3::before{content:"";width:8px;height:8px;background:var(--royal)}
  .about-photo{position:absolute;left:0;right:0;bottom:0;height:200px}
  .tri{position:absolute}
  .mid-photo{height:120px;margin:-22px -18px 0}
  .sub{font-family:"Quicksand",sans-serif;color:var(--sky);font-size:17px;margin:8px 0 8px}
  .body p{margin-bottom:7px}
  .bullets{list-style:none;margin-top:6px}
  .bullets li{position:relative;padding-left:10px;margin-bottom:9px;font-size:7px;line-height:1.45;font-style:italic}
  .bullets li::before{content:"";position:absolute;left:0;top:3px;width:4px;height:4px;border-radius:50%;background:var(--sky)}
  .band{position:absolute;left:0;right:0;bottom:0;height:12px;background:var(--royal);border-top:3px solid var(--sky)}
  .note-heading{font-size:24px;margin-top:6px;width:150px}
  .note-body{font-size:7.4px}
  .note-photo{position:absolute;left:0;right:0;bottom:0;height:205px}
  .price-title{font-family:"Open Sans",sans-serif;font-style:italic;font-weight:600;color:var(--royal);font-size:19px;margin-top:10px}
  .price-row{display:flex;align-items:baseline;gap:4px;padding:3px 6px;font-size:10px;font-style:italic}
  .price-row:nth-child(odd){background:var(--pale);color:var(--sky)}
  .price-row:nth-child(even){color:var(--royal);font-weight:600}
  .price-row .dots{flex:1;border-bottom:1.5px dotted currentColor}
  .price-body{margin-top:10px}
  .brand{display:flex;align-items:center;gap:6px;font-family:"Open Sans",sans-serif;font-weight:700;color:var(--royal);font-size:9px;letter-spacing:.5px;text-transform:uppercase}
  .brand::before{content:"";width:12px;height:12px;background:var(--royal)}
  .shield{display:block;margin:16px auto 10px}
  .center{text-align:center}
  .pill{display:inline-block;border:1px solid var(--light);border-radius:14px;padding:3px 22px;color:var(--royal);font-style:italic;font-size:12px;margin:12px 0 14px}
  .contact dt{font-size:7px;font-weight:700;font-style:italic;color:var(--royal);margin-top:10px}
  .contact dd{font-size:7px;font-style:italic}
  .cover{padding:22px 0 0}
  .cover .brand{padding:0 18px}
  .banner{margin:14px 0 0 12px;background:var(--royal);color:#fff;font-family:"Ubuntu",sans-serif;font-weight:700;font-size:19px;line-height:1.05;padding:10px 12px;border-right:12px solid var(--sky)}
  .cover-photo{height:160px;margin:14px 0 0 12px}
  .call{margin:14px 0 0 0;background:var(--royal);color:#fff;padding:10px 14px 10px 60px;position:relative;font-family:"Ubuntu",sans-serif}
  .call::before{content:"";position:absolute;left:14px;top:14px;width:30px;height:24px;background:var(--sky);border:3px solid #fff}
  .call small{display:block;font-size:12px;font-weight:500}
  .call strong{display:flex;align-items:center;gap:6px;font-size:18px}
  .addr{padding:12px 18px 0;color:var(--royal);font-family:"Ubuntu",sans-serif;font-weight:500;font-size:10px;text-align:right;line-height:1.5}
  .cover .band{height:14px}
</style>
</head>
<body>

<section class="spread spread--inside">
  <article class="panel about">
    <h2 class="heading">About Us</h2>
    <div class="rule"></div>
    <div class="item"><h3>LOREM IPSUM</h3><p class="body">Lorem ipsum is simply dummy text of the printing and typesetting industry. Lorem ipsum has been the industry's standard dummy text ever since the 1500s.</p></div>
    <div class="item"><h3>LOREM IPSUM</h3><p class="body">Lorem ipsum is simply dummy text of the printing and typesetting industry. Lorem ipsum has been the industry's standard dummy text ever since the 1500s.</p></div>
    <div class="item"><h3>LOREM IPSUM</h3><p class="body">Lorem ipsum is simply dummy text of the printing and typesetting industry. Lorem ipsum has been the industry's standard dummy text ever since the 1500s.</p></div>
    <div class="item"><h3>LOREM IPSUM</h3><p class="body">Lorem ipsum is simply dummy text of the printing and typesetting industry. Lorem ipsum has been the industry's standard dummy text ever since the 1500s.</p></div>
    <div class="about-photo photo" role="img" aria-label="Photo of the medical team in white coats and scrubs"></div>
    <svg class="tri" style="left:0;bottom:0" width="110" height="200" viewBox="0 0 110 200"><polygon points="0,40 0,200 110,200" fill="var(--sky)" opacity=".85"/><polygon points="0,0 8,0 100,200 90,200" fill="var(--royal)"/></svg>
  </article>

  <article class="panel inside-mid">
    <div class="mid-photo photo" role="img" aria-label="Photo of a surgeon in an operating theatre"></div>
    <svg class="tri" style="left:0;top:0" width="110" height="80" viewBox="0 0 110 80"><polygon points="0,0 110,0 0,80" fill="var(--sky)"/><polygon points="70,0 90,0 20,60 10,55" fill="var(--royal)"/></svg>
    <h2 class="sub">Your Title here</h2>
    <div class="body">
      <p>Lorem ipsum is simply dummy text of the printing and typesetting industry. Lorem ipsum has been the industry's standard dummy text ever since the 1500s, when an unknown printer took a galley of type and scrambled it to make a type specimen book.</p>
      <p>Lorem ipsum is simply dummy text of the printing and typesetting industry. Lorem ipsum has been the industry's standard dummy text ever since the 1500s, when an unknown printer took a galley of type and scrambled it to make a type specimen book.</p>
    </div>
    <ul class="bullets">
      <li>Lorem ipsum is simply dummy text of the printing and typesetting industry. Lorem ipsum has been the industry's standard text.</li>
      <li>Lorem ipsum is simply dummy text of the printing and typesetting industry. Lorem ipsum has been the industry's standard text.</li>
      <li>Lorem ipsum is simply dummy text of the printing and typesetting industry. Lorem ipsum has been the industry's standard text.</li>
      <li>Lorem ipsum is simply dummy text of the printing and typesetting industry. Lorem ipsum has been the industry's standard text.</li>
    </ul>
    <div class="band"></div>
  </article>

  <article class="panel note">
    <svg class="tri" style="right:0;top:0" width="90" height="120" viewBox="0 0 90 120"><polygon points="10,0 90,0 90,120" fill="var(--sky)"/><polygon points="0,0 10,0 90,110 90,120" fill="var(--royal)"/></svg>
    <h2 class="heading note-heading">Note with patients</h2>
    <div class="rule"></div>
    <div class="body note-body">
      <p>Lorem ipsum is simply dummy text of the printing and typesetting industry. Lorem ipsum has been the industry's standard dummy text ever since the 1500s, when an unknown printer took a galley of type and scrambled it to make a type specimen book. It has survived five centuries and the leap into electronic typesetting.</p>
      <p>Lorem ipsum is simply dummy text of the printing and typesetting industry. Lorem ipsum has been the industry's standard dummy text ever since the 1500s, when an unknown printer took a galley of type and scrambled it to make a type specimen book.</p>
    </div>
    <div class="note-photo photo" role="img" aria-label="Photo of doctors seated at a meeting table"></div>
  </article>
</section>

<section class="spread spread--outside">
  <article class="panel prices">
    <svg class="tri" style="left:0;top:0" width="253" height="14" viewBox="0 0 253 14"><rect x="30" y="0" width="223" height="6" fill="var(--royal)"/><rect x="30" y="6" width="223" height="4" fill="var(--light)"/><rect x="0" y="0" width="22" height="10" fill="var(--sky)"/></svg>
    <h2 class="price-title">Price list</h2>
    <div class="rule"></div>
    <div class="price-list">
      <div class="price-row"><span>Lorem Ipsum</span><span class="dots"></span><span>$ 250</span></div>
      <div class="price-row"><span>Lorem Ipsum</span><span class="dots"></span><span>$ 250</span></div>
      <div class="price-row"><span>Lorem Ipsum</span><span class="dots"></span><span>$ 250</span></div>
      <div class="price-row"><span>Lorem Ipsum</span><span class="dots"></span><span>$ 250</span></div>
      <div class="price-row"><span>Lorem Ipsum</span><span class="dots"></span><span>$ 250</span></div>
      <div class="price-row"><span>Lorem Ipsum</span><span class="dots"></span><span>$ 250</span></div>
      <div class="price-row"><span>Lorem Ipsum</span><span class="dots"></span><span>$ 250</span></div>
      <div class="price-row"><span>Lorem Ipsum</span><span class="dots"></span><span>$ 250</span></div>
      <div class="price-row"><span>Lorem Ipsum</span><span class="dots"></span><span>$ 250</span></div>
    </div>
    <div class="body price-body">
      <p>Lorem ipsum is simply dummy text of the printing and typesetting industry. Lorem ipsum has been the industry's standard dummy text ever since the 1500s, when an unknown printer took a galley of type.</p>
      <p>Lorem ipsum is simply dummy text of the printing and typesetting industry. Lorem ipsum has been the industry's standard dummy text ever since the 1500s, when an unknown printer took a galley of type.</p>
    </div>
    <div class="band"></div>
  </article>

  <article class="panel info">
    <div class="brand">RCH Riverside Care Hospital</div>
    <svg class="shield" width="150" height="165" viewBox="0 0 150 165" role="img" aria-label="Photo of two nurses in scrubs">
      <defs><linearGradient id="shieldFill" x1="0" y1="0" x2="1" y2="1"><stop offset="0" stop-color="#eef4f8"/><stop offset="1" stop-color="#a9cfe0"/></linearGradient></defs>
      <path d="M20 8 L145 2 L140 110 Q120 150 75 162 Q20 140 6 100 Z" fill="url(#shieldFill)" stroke="var(--light)" stroke-width="1.5"/>
    </svg>
    <p class="body center">Lorem ipsum is simply dummy text of the printing and typesetting industry. Lorem ipsum has been the industry's standard dummy text ever since the 1500s.</p>
    <div class="center"><span class="pill">Contact us</span></div>
    <dl class="contact center">
      <dt>Phone</dt><dd>123.345.5690</dd><dd>123.456.1256</dd>
      <dt>web</dt><dd>www.riversidecarehospital.com</dd><dd>info@riversidecarehospital.com</dd>
      <dt>Address</dt><dd>Dummy city</dd><dd>Dummy Country, Dummy land</dd>
    </dl>
  </article>

  <article class="panel cover">
    <div class="brand">RCH Riverside Care Hospital</div>
    <h1 class="banner">WE CARE ABOUT<br>YOUR HEALTH</h1>
    <div class="cover-photo photo" role="img" aria-label="Photo of smiling doctors and nurses"></div>
    <div class="call">
      <small>Contact us today</small>
      <strong><svg width="14" height="14" viewBox="0 0 24 24"><path d="M6.6 10.8a15 15 0 0 0 6.6 6.6l2.2-2.2a1 1 0 0 1 1-.25 11.4 11.4 0 0 0 3.6.57 1 1 0 0 1 1 1V20a1 1 0 0 1-1 1A17 17 0 0 1 3 4a1 1 0 0 1 1-1h3.5a1 1 0 0 1 1 1c0 1.25.2 2.45.57 3.57a1 1 0 0 1-.25 1z" fill="#fff"/></svg>1-234-567890</strong>
    </div>
    <p class="addr">Dummy city, Dummy Country Land<br>www.riversidecarehospital.com</p>
    <div class="band"></div>
  </article>
</section>

</body>
</html>
```